LETTERPRESS Greeting Card Design Project

Looking for greeting card designs for letterpress printing
We would like designs that are simple and clean.
1-3 colors light "spring" colors
SIZE: A2 Folded cards.
Floral designs
Valentines day cards.
Thank you notes
Happy birthday cards
Final files separated on layers for each color. as AI vector format.
Include fonts and type used in design.
Project Deadline Extended

```html
<!DOCTYPE html>
<html lang="en">
<head>
<meta charset="UTF-8">
<title>Love — Letterpress Valentine Card</title>
<link rel="stylesheet" href="https://fonts.googleapis.com/css2?family=Great+Vibes&display=swap">
<style>
  :root {
    --backdrop: #ffffff;
    --card-cream: #e9dbbb;
    --heart-coral: #d9605b;
    --heart-edge: #b84a45;
    --lettering-cream: #ecdcbc;
    --sprig-coral: #dc6a63;
  }

  * { margin: 0; padding: 0; box-sizing: border-box; }

  html, body {
    width: 1200px;
    height: 900px;
    overflow: hidden;
    background: var(--backdrop);
  }

  .canvas {
    position: relative;
    width: 1200px;
    height: 900px;
  }

  .card-front {
    position: absolute;
    left: 342px;
    top: 82px;
    width: 516px;
    height: 736px;
    background: var(--card-cream);
    overflow: hidden;
  }

  .floral-sprig {
    position: absolute;
  }

  .floral-sprig--top-left {
    left: 0;
    top: 0;
    width: 190px;
    height: 195px;
    background: radial-gradient(ellipse at 35% 40%, rgba(220, 106, 99, 0.35) 0%, rgba(220, 106, 99, 0.12) 55%, rgba(220, 106, 99, 0) 75%);
  }

  .floral-sprig--bottom-right {
    right: 0;
    bottom: 0;
    width: 195px;
    height: 235px;
    background: radial-gradient(ellipse at 60% 60%, rgba(220, 106, 99, 0.35) 0%, rgba(220, 106, 99, 0.12) 55%, rgba(220, 106, 99, 0) 75%);
  }

  .love-heart {
    position: absolute;
    left: 76px;
    top: 197px;
    width: 366px;
    height: 356px;
  }

  .love-heart__shape { fill: var(--heart-coral); }
  .love-heart__edge { fill: var(--heart-edge); }

  .love-heart__word {
    position: absolute;
    left: 0;
    top: 68px;
    width: 100%;
    text-align: center;
    font-family: "Great Vibes", cursive;
    font-size: 132px;
    line-height: 1;
    color: var(--lettering-cream);
    padding-left: 12px;
  }
</style>
</head>
<body>
  <main class="canvas">
    <section class="card-front">
      <div class="floral-sprig floral-sprig--top-left" role="img" aria-label="Coral leafy floral sprig growing down from the top-left corner"></div>

      <div class="love-heart">
        <svg width="366" height="356" viewBox="0 0 366 356" aria-hidden="true">
          <path class="love-heart__edge" d="M183 67 C150 12 90 2 45 27 C5 52 -5 107 10 152 C35 227 130 287 183 357 C236 287 331 227 356 152 C371 107 361 52 321 27 C276 2 216 12 183 67Z"/>
          <path class="love-heart__shape" d="M183 60 C150 5 90 -5 45 20 C5 45 -5 100 10 145 C35 220 130 280 183 350 C236 280 331 220 356 145 C371 100 361 45 321 20 C276 -5 216 5 183 60Z"/>
        </svg>
        <p class="love-heart__word">Love</p>
      </div>

      <div class="floral-sprig floral-sprig--bottom-right" role="img" aria-label="Coral leafy floral sprig growing up from the bottom-right corner"></div>
    </section>
  </main>
</body>
</html>
```